Orthopaedic Clinic Needs facebook page

Orthopaedic Clinic needs facebook page. The name of our clinic is Corvale & Lune Orthopaedics. We focus on hip and knee orthopaedic conditions, as well as general orthopaedics. The main services are total knee replacements, total hip replacements, sports injury of the knee, hip fractures. Unique selling points of our service would be 1. Patient Centred Care, 2. Value Driven, 3. 2 Double-Fellowship Trained Surgeons.

Colour scheme should fit the logo design and be within the general colour recommendations of a medical clinic.

The design should be modern, eye catching, draws the end user to the website.

We would like to design our facebook page for future social media marketing.
In accordance with local advertisement regulations pertaining to medical clinics, no statements must have any information or laudatory statements such as the use of best, better, breakthrough, champions, or any statements that imply superiority and that may create unjustified expectations of services.

Target Market(s)

Patients
Friends family and relatives of patients.

Font styles to use
Serif
Sans Serif

Requirements
Must have
• My project must have my logo.

A nice colour scheme comfortable to the eye.
Nice to have
• Nice eye catching design that will draw the end user to the page.
Should not have
• Must not have any information that create unjustified expectaions.
Must not contain laudatory statements such as best, better, breakthrough, champions, or other statement that may create unjustified expecation of services.

```html
<!DOCTYPE html>
<html lang="en">
<head>
<meta charset="utf-8">
<title>Corvale &amp; Lune Orthopaedics – Facebook Cover</title>
<link rel="stylesheet" href="https://fonts.googleapis.com/css2?family=Open+Sans:wght@400;700&family=Oswald:wght@400&family=Montserrat:wght@400&display=swap">
<style>
  :root {
    --page-bg: #eceeee;
    --card-bg: #ffffff;
    --soft-grey: #e7e8e8;
    --teal: #5bb5ad;
    --ink: #1d1f20;
    --text-grey: #3d3f40;
    --icon-grey: #555758;
    --arc-dark: #2c3b40;
    --photo-tone: #a7b2b0;
  }
  * { margin: 0; padding: 0; box-sizing: border-box; }
  html, body { width: 1200px; height: 787px; overflow: hidden; background: var(--page-bg); }
  .cover {
    position: absolute; left: 0; top: 165px;
    width: 1200px; height: 457px;
    background: radial-gradient(ellipse at 55% 45%, var(--soft-grey) 0%, var(--card-bg) 60%);
    overflow: hidden;
  }
  .cover-art { position: absolute; left: 0; top: 0; width: 1200px; height: 386px; }
  .brand {
    position: absolute; left: 70px; top: 27px;
    display: flex; align-items: center; gap: 16px;
  }
  .brand-square { width: 66px; height: 66px; background: var(--teal); flex: none; }
  .brand-name {
    font-family: "Montserrat", sans-serif; font-weight: 400;
    color: var(--text-grey); line-height: 1.05; text-transform: uppercase;
    white-space: nowrap;
  }
  .brand-name .line-1 { display: block; font-size: 32px; letter-spacing: 0.5px; }
  .brand-name .line-2 { display: block; font-size: 19px; letter-spacing: 5px; margin-top: 4px; }
  .section-title {
    position: absolute; left: 70px; top: 118px;
    font-family: "Oswald", sans-serif; font-weight: 400;
    font-size: 46px; line-height: 1; color: var(--teal);
  }
  .title-rule { position: absolute; left: 70px; top: 174px; height: 6px; width: 228px; display: flex; }
  .title-rule .dark { width: 64px; background: var(--arc-dark); }
  .title-rule .light { flex: 1; background: var(--teal); height: 3px; margin-top: 1px; }
  .services {
    position: absolute; left: 72px; top: 198px; list-style: none;
    font-family: "Open Sans", sans-serif; font-size: 30px; color: var(--text-grey);
    white-space: nowrap;
  }
  .services li { display: flex; align-items: center; height: 41.5px; }
  .services svg { width: 20px; height: 20px; margin-right: 18px; flex: none; }
  .usp-band {
    position: absolute; left: 0; top: 386px; width: 1200px; height: 71px;
    background: var(--teal); display: flex; align-items: center; padding-left: 70px;
    font-family: "Open Sans", sans-serif; font-weight: 700; font-size: 28px; color: var(--ink);
    white-space: nowrap;
  }
</style>
</head>
<body>
  <section class="cover">
    <svg class="cover-art" viewBox="0 0 1200 386">
      <path class="arc-band" d="M766,0 Q590,190 722,386 L1200,386 L1200,0 Z" fill="var(--arc-dark)"/>
      <path class="photo-area" role="img" aria-label="Photo of a runner on a country road holding her knee in pain"
            d="M782,0 Q612,195 738,386 L1200,386 L1200,0 Z" fill="var(--photo-tone)"/>
    </svg>

    <div class="brand">
      <div class="brand-square"></div>
      <div class="brand-name"><span class="line-1">Corvale &amp; Lune</span><span class="line-2">Orthopaedics</span></div>
    </div>

    <h2 class="section-title">What we do</h2>
    <div class="title-rule"><span class="dark"></span><span class="light"></span></div>

    <ul class="services">
      <li><svg viewBox="0 0 20 20"><circle cx="10" cy="10" r="8" fill="none" stroke="var(--icon-grey)" stroke-width="1.6"/><path d="M6 10l3 3 6-7" fill="none" stroke="var(--icon-grey)" stroke-width="1.8"/></svg>Total knee replacements</li>
      <li><svg viewBox="0 0 20 20"><circle cx="10" cy="10" r="8" fill="none" stroke="var(--icon-grey)" stroke-width="1.6"/><path d="M6 10l3 3 6-7" fill="none" stroke="var(--icon-grey)" stroke-width="1.8"/></svg>Total hip replacements</li>
      <li><svg viewBox="0 0 20 20"><circle cx="10" cy="10" r="8" fill="none" stroke="var(--icon-grey)" stroke-width="1.6"/><path d="M6 10l3 3 6-7" fill="none" stroke="var(--icon-grey)" stroke-width="1.8"/></svg>Sports injury of the knee</li>
      <li><svg viewBox="0 0 20 20"><circle cx="10" cy="10" r="8" fill="none" stroke="var(--icon-grey)" stroke-width="1.6"/><path d="M6 10l3 3 6-7" fill="none" stroke="var(--icon-grey)" stroke-width="1.8"/></svg>Hip fractures</li>
    </ul>

    <div class="usp-band">Patient Centred Care&nbsp;|&nbsp;Value Driven&nbsp;|&nbsp;2 Double-Fellowship Trained Surgeons</div>
  </section>
</body>
</html>
```